KLT Website Homepage Redesign

My website needs a homepage redesign and banner photos updates for Discovery and SEO Services pages. We sell Search Engine Optimization services. We use Search Engine Optimization techniques to help our clients rank high in search engines like Zorvix. It is an intense competition to consistently rank above other businesses. The problem is there is no easy way to show what the benefits of Search Engine Optimization services look like in an emotional way. I want to use an image from sailboat racing to dramatize that our clients win at Search Engine Optimization marketing.
The following products are desired:
1. Desktop version homepage redesign with a banner that clearly shows we sell Search Engine Optimization services using sailboat racing as a metaphor.
2. Mobile version homepage redesign with a banner that clearly shows we sell Search Engine Optimization services using sailboat racing as a metaphor.
2. New banner photo for the Discovery Page
3. New banner photo for the SEO page
The design must be responsive and show well on desktops, laptops, tablets and mobile phones. The current footer style must be kept. A third service called SEO must be added.
the website URL is www.velmorbix.com
Target Market(s)
Business to Business
Industry/Entity Type
Digital Marketing
Coding
Coded - Design and coding required
Number of Pages Required
1 page
Colors
Designer to choose colors to be used in the design.
Look and feel
Each slider illustrates characteristics of the customer's brand and the style your logo design should communicate.

```html
<!DOCTYPE html>
<html lang="en">
<head>
<meta charset="utf-8">
<title>KLT – Contact</title>
<link href="https://fonts.googleapis.com/css2?family=Poppins:wght@500;600;700&family=Lato:wght@400&family=Mulish:wght@400;600&display=swap" rel="stylesheet">
<style>
  :root {
    --page-white: #ffffff;
    --section-bg: #eaf2fb;
    --ink: #141414;
    --label: #2b2b3a;
    --orange: #ff5a1f;
    --amber: #ffc65a;
    --placeholder: #4a4a55;
    --field-border: #dfe7f1;
    --faint: #d6e3f2;
    --navy: #1b2a64;
  }
  * { box-sizing: border-box; margin: 0; padding: 0; }
  html, body { width: 1200px; height: 1010px; overflow: hidden; background: var(--page-white); }
  .canvas { position: relative; width: 1200px; height: 1010px; overflow: hidden; }

  .contact-section { position: absolute; left: 0; top: 21px; width: 1200px; height: 596px; background: var(--section-bg); }
  .eyebrow { position: absolute; top: 61px; width: 100%; text-align: center; font: 500 12.5px Poppins, sans-serif; color: var(--label); }
  .eyebrow .brace { color: var(--orange); font-weight: 400; font-size: 16px; margin: 0 4px; }
  .headline { position: absolute; top: 82px; width: 100%; text-align: center; font: 700 32px/36px Poppins, sans-serif; color: var(--ink); letter-spacing: -0.5px; }

  .illustration { position: absolute; left: 244px; top: 186px; width: 334px; height: 290px; border-radius: 18px;
    background: radial-gradient(ellipse at 55% 50%, #3f6ae6 0%, #7b9cf0 45%, #c9d9f6 75%, rgba(234,242,251,0) 100%); }

  .field { position: absolute; background: #fff; border: 1px solid var(--field-border); border-radius: 3px;
    font: 400 8px Lato, sans-serif; color: var(--placeholder); padding: 10px 0 0 15px; }
  .field-first { left: 611px; top: 188px; width: 162px; height: 31px; }
  .field-last  { left: 789px; top: 188px; width: 162px; height: 31px; }
  .field-mail  { left: 611px; top: 237px; width: 162px; height: 31px; }
  .field-phone { left: 789px; top: 237px; width: 162px; height: 31px; }
  .field-message { left: 611px; top: 285px; width: 338px; height: 88px; padding-top: 10px; }

  .send-button { position: absolute; left: 611px; top: 390px; width: 340px; height: 37px; border-radius: 3px;
    background: linear-gradient(90deg, #ff5a1f 0%, #ff5e24 30%, #ffc65a 100%);
    box-shadow: 0 6px 14px rgba(255, 120, 50, 0.3);
    display: flex; align-items: center; justify-content: center; gap: 6px;
    font: 600 9.5px Poppins, sans-serif; color: #fff; }

  .info-item { position: absolute; top: 490px; color: var(--faint); font-family: Mulish, sans-serif; }
  .info-item svg { position: absolute; left: -22px; top: 0; }
  .info-title { font-size: 15px; font-weight: 400; }
  .info-line { font-size: 8px; margin-top: 6px; line-height: 8px; }
  .info-address { left: 341px; }
  .info-mail { left: 592px; }
  .info-call { left: 792px; }

  .site-footer { position: absolute; left: 0; top: 617px; width: 1200px; height: 372px; color: var(--navy); font-family: Mulish, sans-serif; }
  .footer-scene { position: absolute; inset: 0;
    background: linear-gradient(180deg, #cfdcea 0%, #c3d2e3 45%, #a9bfd6 70%, #93aecb 100%); }
  .footer-heading { position: absolute; top: 44px; font-size: 24px; font-weight: 400; letter-spacing: 3px; transform: translateX(-50%); white-space: nowrap; }
  .heading-lead { left: 327px; }
  .heading-links { left: 873px; }
  .contact-label { position: absolute; left: 72px; top: 98px; font-size: 18px; font-weight: 600; }
  .address { position: absolute; left: 72px; top: 132px; font-size: 18px; line-height: 24px; font-style: normal; }
  .link-list { position: absolute; top: 99px; list-style: none; font-size: 18px; line-height: 33px; }
  .link-list-main { left: 618px; }
  .link-list-services { left: 874px; }
  .copyright { position: absolute; top: 276px; width: 100%; text-align: center; font-size: 18px; }
</style>
</head>
<body>
<div class="canvas">
  <section class="contact-section">
    <p class="eyebrow"><span class="brace">{</span>Contact us<span class="brace">}</span></p>
    <h1 class="headline">Want to hire us to boost site<br>contact us any time!</h1>

    <div class="illustration" role="img" aria-label="Illustration of a team working around large blue SEO letters with a browser window, star badge and gear"></div>

    <div class="field field-first">First name *</div>
    <div class="field field-last">Last name *</div>
    <div class="field field-mail">Your mail *</div>
    <div class="field field-phone">Phone number *</div>
    <div class="field field-message">Message...</div>
    <div class="send-button">
      <svg width="10" height="10" viewBox="0 0 10 10"><circle cx="5" cy="5" r="5" fill="#fff"/><path d="M3 5h4M5.3 3.2L7 5 5.3 6.8" stroke="#ff5a1f" stroke-width="1.2" fill="none"/></svg>
      Send now
    </div>

    <div class="info-item info-address">
      <svg width="18" height="22" viewBox="0 0 18 22"><path d="M9 1a7 7 0 0 0-7 7c0 5 7 12 7 12s7-7 7-12a7 7 0 0 0-7-7z" fill="none" stroke="#d6e3f2" stroke-width="1.5"/><circle cx="9" cy="8" r="2.5" fill="none" stroke="#d6e3f2" stroke-width="1.5"/></svg>
      <div class="info-title">Our office address</div>
      <div class="info-line">2084 Harbor Crest Pkwy</div>
      <div class="info-line">Marlowe, MD 21977</div>
    </div>
    <div class="info-item info-mail">
      <svg width="20" height="18" viewBox="0 0 20 18"><rect x="1" y="3" width="18" height="12" rx="1" fill="none" stroke="#d6e3f2" stroke-width="1.5"/><path d="M1 4l9 6 9-6" fill="none" stroke="#d6e3f2" stroke-width="1.5"/></svg>
      <div class="info-title">Mail Us</div>
      <div class="info-line">hello@velmorbix.com</div>
      <div class="info-line">support@velmorbix.com</div>
    </div>
    <div class="info-item info-call">
      <svg width="18" height="20" viewBox="0 0 18 20"><path d="M4 2l3 4-2 2c1 3 3 5 6 6l2-2 4 3-2 3C8 18 1 11 1 4z" fill="none" stroke="#d6e3f2" stroke-width="1.5"/></svg>
      <div class="info-title">Call for help</div>
      <div class="info-line">+1 410 555 0182</div>
      <div class="info-line">Mon to Fri, 9am to 6pm</div>
    </div>
  </section>

  <footer class="site-footer">
    <div class="footer-scene" role="img" aria-label="Faded photograph of sailboats racing on open water with hills behind"></div>
    <h2 class="footer-heading heading-lead">TAKE THE LEAD</h2>
    <h2 class="footer-heading heading-links">USEFUL LINKS</h2>
    <p class="contact-label">Contact Us</p>
    <address class="address">2084 Harbor Crest Pkwy<br>Suite 410B<br>Marlowe, MD 21977</address>
    <ul class="link-list link-list-main">
      <li>Home</li><li>Web Strategy</li><li>Support</li><li>Privacy</li>
    </ul>
    <ul class="link-list link-list-services">
      <li>SEO</li><li>Advanced Website Tools</li><li>Testimonials</li><li>Terms of Use</li>
    </ul>
    <p class="copyright">© 2019 Kaltren Applications | All Rights Reserved | Web Strategy by Kaltren Applications</p>
  </footer>
</div>
</body>
</html>
```